Creative Business Card for my Sail Boat.. Tide & Drift

Going to order PLASTIC business cards for my boat.. she is a sailing vessel catamaran named Tide & Drift..

Target Market(s)

to impress other boaters with a unique designed plastic card

Contact Information for Business Card

S/V Tide & Drift
Captain Carl Denby
denby@carl.example
Mobile/WhatsApp 1-555-318-7620
www.sailtideanddrift.example

Requirements
Must have
• Cool colors. logo.. and info in Business Card Details.. Thanks! Utilize clear or cloudy plastic in design. Thanks

```html
<!DOCTYPE html>
<html lang="en">
<head>
<meta charset="utf-8">
<title>Tide &amp; Drift – Business Card</title>
<link href="https://fonts.googleapis.com/css2?family=Arvo:wght@700&family=Inter:wght@400&display=swap" rel="stylesheet">
<style>
  :root {
    --backdrop: #bdbdbd;
    --card-red: #c42027;
    --card-red-haze: rgba(255, 255, 255, 0.10);
    --card-frost: rgba(255, 255, 255, 0.88);
    --card-frost-edge: rgba(255, 255, 255, 0.55);
    --frost-tint: rgba(226, 240, 232, 0.55);
    --brand-beige: #b7aaa0;
    --brand-brown: #5a2a14;
    --accent-green: #2e9a48;
    --accent-red: #c42027;
    --text-dark: #3a3a3a;
  }
  * { margin: 0; padding: 0; box-sizing: border-box; }
  html, body { width: 1200px; height: 900px; overflow: hidden; }
  body {
    background: var(--backdrop);
    font-family: "Inter", Helvetica, Arial, sans-serif;
    position: relative;
  }
  .card {
    position: absolute;
    left: 285px;
    width: 630px;
    height: 360px;
    border-radius: 34px;
    box-shadow: 0 6px 14px rgba(0,0,0,0.25);
    overflow: hidden;
  }
  /* front: tinted plastic with a soft cloudy sheen */
  .card--front {
    top: 45px;
    background:
      radial-gradient(ellipse 60% 70% at 50% 45%, var(--card-red-haze), transparent 70%),
      linear-gradient(160deg, rgba(255,255,255,0.08), transparent 45%),
      var(--card-red);
  }
  /* back: cloudy frosted plastic */
  .card--back {
    top: 495px;
    background:
      radial-gradient(ellipse 55% 80% at 80% 40%, var(--frost-tint), transparent 70%),
      linear-gradient(150deg, var(--card-frost-edge), transparent 35%),
      var(--card-frost);
    border: 1px solid rgba(255,255,255,0.7);
  }

  .brand {
    display: flex;
    align-items: center;
    gap: 14px;
    font-family: "Arvo", Georgia, serif;
    font-weight: 700;
  }
  .brand__dot {
    border-radius: 50%;
    background: var(--accent-green);
    flex: none;
  }
  .card--front .brand {
    position: absolute;
    inset: 0;
    justify-content: center;
    font-size: 62px;
    color: var(--brand-beige);
  }
  .card--front .brand__dot { width: 46px; height: 46px; }

  .card--back .brand {
    position: absolute;
    left: 40px; top: 48px;
    font-size: 48px;
    color: var(--brand-brown);
  }
  .card--back .brand__dot { width: 36px; height: 36px; }

  .person { position: absolute; left: 40px; top: 170px; }
  .person__name {
    font-family: "Arvo", Georgia, serif;
    font-weight: 700;
    font-size: 34px;
    color: var(--brand-brown);
    line-height: 1.1;
  }
  .person__role { font-size: 18px; color: var(--text-dark); margin-top: 2px; }

  .contact { list-style: none; margin-top: 14px; }
  .contact__item {
    display: flex; align-items: center; gap: 10px;
    font-size: 17px; color: var(--text-dark);
    line-height: 1.5;
  }
  .contact__icon { width: 18px; height: 18px; flex: none; }
  .contact__domain { color: var(--accent-red); }

  .mobile-line {
    position: absolute;
    right: 36px; top: 150px;
    display: flex; align-items: center; gap: 8px;
    font-size: 15px; color: var(--text-dark);
    letter-spacing: 1px;
  }
  .mobile-line__dot {
    width: 16px; height: 16px; border-radius: 50%;
    background: var(--accent-green);
  }
</style>
</head>
<body>
  <section class="card card--front" aria-label="Card front">
    <div class="brand">
      <span class="brand__name">Tide &amp; Drift</span>
      <span class="brand__dot"></span>
    </div>
  </section>

  <section class="card card--back" aria-label="Card back">
    <div class="brand">
      <span class="brand__name">Tide &amp; Drift</span>
      <span class="brand__dot"></span>
    </div>

    <div class="mobile-line">
      <span>1-555-318-7620</span>
      <span class="mobile-line__dot"></span>
    </div>

    <div class="person">
      <p class="person__name">Carl Denby</p>
      <p class="person__role">Captain</p>
      <ul class="contact">
        <li class="contact__item">
          <svg class="contact__icon" viewBox="0 0 20 20"><rect x="1" y="4" width="18" height="12" fill="var(--brand-brown)"/><path d="M1 4 L10 11 L19 4" stroke="#fff" stroke-width="1.5" fill="none"/></svg>
          <span>denby@carl.example</span>
        </li>
        <li class="contact__item">
          <svg class="contact__icon" viewBox="0 0 20 20"><rect x="5" y="1.5" width="10" height="17" rx="2" fill="none" stroke="var(--brand-brown)" stroke-width="1.8"/><circle cx="10" cy="15.5" r="1" fill="var(--brand-brown)"/></svg>
          <span>1-555-318-7620</span>
        </li>
        <li class="contact__item">
          <svg class="contact__icon" viewBox="0 0 20 20"><g fill="none" stroke="var(--brand-brown)" stroke-width="1.6"><circle cx="10" cy="10" r="8"/><ellipse cx="10" cy="10" rx="3.5" ry="8"/><path d="M2 10 H18 M3.5 6 H16.5 M3.5 14 H16.5"/></g></svg>
          <span>www.<span class="contact__domain">sailtideanddrift</span>.example</span>
        </li>
      </ul>
    </div>
  </section>
</body>
</html>
```